Business card for law firm

Need business card for new law firm. Think confident, authoritative, conservative, but not stuffy or old-fashioned.

Contact Information for Business Card

Content for card - logo (uploaded), plus the following:

Paul Wexbury (larger font)
Managing Partner (larger font, but not as large as name)
Level 9, 41 Tansy Lane
Sydney NSW 2000
Main Tel 02 7346 2190
Direct Tel 02 6273 4415
Email paul@qvlegal.com.au
www.qvlegal.com.au

Letterhead design should include logo plus:
Level 9, 41 Tansy Lane
Sydney NSW 2000
Tel 02 6273 4415
www.qvlegal.com.au

```html
<!DOCTYPE html>
<html lang="en">
<head>
<meta charset="utf-8">
<title>Quayvale Lawyers – Business Card</title>
<link rel="stylesheet" href="https://fonts.googleapis.com/css2?family=Marcellus&family=Noto+Serif:wght@400;700&display=swap">
<style>
  :root {
    --navy: #22265a;
    --navy-deep: #1f2352;
    --white: #ffffff;
    --page: #e9eaec;
    --soft-white: #e6e7f0;
  }
  * { margin: 0; padding: 0; box-sizing: border-box; }
  html, body {
    width: 1154px;
    height: 1200px;
    overflow: hidden;
    background: var(--page);
  }
  .sheet {
    position: relative;
    width: 1154px;
    height: 1200px;
  }
  .card {
    position: absolute;
    width: 520px;
    height: 850px;
    background: var(--navy);
    box-shadow: 0 4px 14px rgba(0, 0, 0, 0.25);
    color: var(--white);
    overflow: hidden;
  }

  /* Front */
  .card--front {
    left: 40px;
    top: 60px;
    border-top: 68px solid var(--white);
  }
  .front-brand {
    position: absolute;
    left: 0;
    right: 0;
    top: 262px;
    text-align: center;
    font-family: "Marcellus", serif;
    font-weight: 400;
    color: var(--white);
  }
  .brand-mark {
    width: 96px;
    height: 96px;
    margin: 0 auto 46px;
    background: var(--white);
  }
  .brand-name {
    font-size: 58px;
    letter-spacing: 2px;
    line-height: 1;
  }
  .brand-sub {
    font-size: 24px;
    letter-spacing: 27px;
    margin-top: 14px;
    padding-left: 27px;
    line-height: 1;
  }
  .front-web {
    position: absolute;
    left: 0;
    right: 0;
    bottom: 58px;
    text-align: center;
    font-family: "Noto Serif", serif;
    font-size: 23px;
  }

  /* Back */
  .card--back {
    left: 604px;
    top: 300px;
    border-left: 44px solid var(--white);
  }
  .back-brand {
    position: absolute;
    right: 36px;
    top: 56px;
    text-align: center;
    font-family: "Marcellus", serif;
    font-weight: 400;
    color: var(--white);
  }
  .back-brand .brand-mark {
    width: 50px;
    height: 50px;
    margin-bottom: 22px;
  }
  .back-brand .brand-name {
    font-size: 34px;
    letter-spacing: 1px;
  }
  .back-brand .brand-sub {
    font-size: 13px;
    letter-spacing: 15px;
    padding-left: 15px;
    margin-top: 6px;
  }
  .contact {
    position: absolute;
    left: 44px;
    bottom: 48px;
    font-family: "Noto Serif", serif;
    color: var(--white);
  }
  .contact-name {
    font-size: 36px;
    font-weight: 700;
    line-height: 1.05;
  }
  .contact-role {
    font-size: 25px;
    font-weight: 700;
    line-height: 1.1;
    margin-bottom: 28px;
  }
  .contact-address,
  .contact-phones {
    font-size: 23px;
    line-height: 1.3;
    margin-bottom: 18px;
  }
  .phone-label {
    font-size: 14px;
  }
  .contact-email {
    font-size: 23px;
  }
</style>
</head>
<body>
<main class="sheet">
  <section class="card card--front" aria-label="Card front">
    <div class="front-brand">
      <div class="brand-mark"></div>
      <div class="brand-name">QUAYVALE</div>
      <div class="brand-sub">LAWYERS</div>
    </div>
    <p class="front-web">www.qvlegal.com.au</p>
  </section>

  <section class="card card--back" aria-label="Card back">
    <div class="back-brand">
      <div class="brand-mark"></div>
      <div class="brand-name">QUAYVALE</div>
      <div class="brand-sub">LAWYERS</div>
    </div>
    <div class="contact">
      <p class="contact-name">Paul Wexbury</p>
      <p class="contact-role">Managing Partner</p>
      <p class="contact-address">Level 9, 41 Tansy Lane<br>Sydney &bull; NSW &bull; 2000</p>
      <p class="contact-phones">02 7346 2190 <span class="phone-label">(main)</span><br>02 6273 4415 <span class="phone-label">(direct)</span></p>
      <p class="contact-email">paul@qvlegal.com.au</p>
    </div>
  </section>
</main>
</body>
</html>
```